Criação de Papelaria Profissional para Beleza
A empresa queria:
" Atendemos clientes adultos masculino, feminino, adolescentes para tratamentos estéticos diversos como acne, rejuvenescimento facial, redução de medidas faciais e corporais, depilação, tratamento de celulite, estrias, medicina capilar, laser, cicatrizes, manchas, melasma, pequenos vasos, poros dilatados, limpeza de pele "

```html
<!DOCTYPE html>
<html lang="pt-BR">
<head>
<meta charset="UTF-8">
<title>Lumera Clínica Estética – Cartão de Visita</title>
<link rel="stylesheet" href="https://fonts.googleapis.com/css2?family=Cinzel:wght@400&family=Montserrat:wght@400;500&display=swap">
<style>
  :root {
    --bg-top: #2bd3cc;
    --bg-bottom: #8ff0ea;
    --navy: #1a2a5c;
    --teal: #1fc2bd;
    --white: #ffffff;
    --ink: #3a3f4d;
    --muted: #6b7080;
  }
  * { margin: 0; padding: 0; box-sizing: border-box; }
  html, body {
    width: 1200px;
    height: 1200px;
    overflow: hidden;
  }
  body {
    background: linear-gradient(160deg, var(--bg-top), var(--bg-bottom));
    font-family: "Montserrat", sans-serif;
    position: relative;
  }
  .card {
    position: absolute;
    left: 150px;
    width: 900px;
    height: 514px;
    box-shadow: 0 18px 40px rgba(10, 60, 70, 0.25);
  }
  .card-front {
    top: 48px;
    background: var(--navy);
  }
  .card-back {
    top: 620px;
    background: var(--white);
  }
  .brand {
    position: absolute;
    text-align: center;
  }
  .brand-name {
    font-family: "Cinzel", serif;
    font-weight: 400;
    letter-spacing: 0.06em;
    line-height: 1;
  }
  .brand-tagline {
    font-family: "Montserrat", sans-serif;
    font-weight: 400;
    text-transform: uppercase;
    letter-spacing: 0.42em;
    margin-top: 10px;
  }
  .card-front .brand {
    left: 0;
    right: 0;
    top: 200px;
    color: var(--white);
  }
  .card-front .brand-name { font-size: 78px; }
  .card-front .brand-tagline { font-size: 18px; color: var(--white); }

  .card-back .brand {
    left: 70px;
    bottom: 70px;
    color: var(--navy);
  }
  .card-back .brand-name { font-size: 52px; }
  .card-back .brand-tagline { font-size: 12px; color: var(--navy); }

  .contact {
    position: absolute;
    right: 70px;
    top: 70px;
    width: 340px;
  }
  .contact-list { list-style: none; }
  .contact-item {
    display: flex;
    align-items: center;
    gap: 14px;
    font-size: 17px;
    color: var(--ink);
    margin-bottom: 14px;
  }
  .contact-icon {
    width: 26px;
    height: 26px;
    flex: none;
  }
  .divider {
    height: 3px;
    width: 100%;
    background: var(--teal);
    margin: 26px 0 30px;
  }
  .address {
    font-style: normal;
    font-size: 17px;
    line-height: 1.55;
    color: var(--ink);
  }
</style>
</head>
<body>

  <section class="card card-front" aria-label="Frente do cartão">
    <div class="brand">
      <div class="brand-name">LUMERA</div>
      <div class="brand-tagline">Clínica Estética</div>
    </div>
  </section>

  <section class="card card-back" aria-label="Verso do cartão">
    <div class="contact">
      <ul class="contact-list">
        <li class="contact-item">
          <svg class="contact-icon" viewBox="0 0 26 26" aria-hidden="true">
            <circle cx="13" cy="13" r="13" fill="var(--navy)"/>
            <rect x="7" y="8.5" width="12" height="9" rx="1" fill="none" stroke="#fff" stroke-width="1.5"/>
            <path d="M7.5 9.5 L13 14 L18.5 9.5" fill="none" stroke="#fff" stroke-width="1.5"/>
          </svg>
          contato@lumera.com.br
        </li>
        <li class="contact-item">
          <svg class="contact-icon" viewBox="0 0 26 26" aria-hidden="true">
            <circle cx="13" cy="13" r="13" fill="var(--navy)"/>
            <circle cx="13" cy="13" r="6" fill="none" stroke="#fff" stroke-width="1.4"/>
            <path d="M7 13 H19 M13 7 C10 10 10 16 13 19 M13 7 C16 10 16 16 13 19" fill="none" stroke="#fff" stroke-width="1.2"/>
          </svg>
          www.lumera.com.br
        </li>
        <li class="contact-item">
          <svg class="contact-icon" viewBox="0 0 26 26" aria-hidden="true">
            <circle cx="13" cy="13" r="13" fill="var(--navy)"/>
            <path d="M9 7.5 L11.2 7.5 L12.2 10.5 L10.8 11.6 C11.6 13.3 12.7 14.4 14.4 15.2 L15.5 13.8 L18.5 14.8 L18.5 17 C18.5 17.8 17.8 18.5 17 18.5 C12 18.2 7.8 14 7.5 9 C7.5 8.2 8.2 7.5 9 7.5 Z" fill="#fff"/>
          </svg>
          (00) 0000-0000
        </li>
      </ul>
      <div class="divider"></div>
      <address class="address">
        Rua Nome da Rua, 000,<br>
        nome do bairro, nome<br>
        da cidade, UF /<br>
        Cep 00000-000
      </address>
    </div>

    <div class="brand">
      <div class="brand-name">LUMERA</div>
      <div class="brand-tagline">Clínica Estética</div>
    </div>
  </section>

</body>
</html>
```